ZEH Project Signage

Need a sign to be displayed in the front of properties currently under Construction or Renovation to advertise our company information. Need it to be Professional and Contemporary. We are a Design/Build Construction Company. Information should include Company Name, email, website, phone number. Attached: Logo and company brochure, also included and inspiration images

```html
<!DOCTYPE html>
<html lang="en">
<head>
<meta charset="utf-8">
<title>ZEH Construction – Project Sign</title>
<link rel="stylesheet" href="https://fonts.googleapis.com/css2?family=Roboto:wght@400;500&display=swap">
<style>
  :root {
    --page-bg: #ececec;
    --sign-white: #ffffff;
    --brand-yellow: #f0ec45;
    --yellow-glaze: rgba(240, 236, 69, 0.72);
    --icon-olive: #b4b23c;
    --icon-fold: #2b2b1a;
    --ink: #1c1c1c;
    --contour-bg: #f2f2f2;
  }
  * { margin: 0; padding: 0; box-sizing: border-box; }
  html, body {
    width: 1200px; height: 1200px; overflow: hidden;
    background: var(--page-bg);
    font-family: "Roboto", Arial, sans-serif;
    color: var(--ink);
  }
  .sign {
    position: absolute; left: 237px; top: 55px;
    width: 726px; height: 1089px;
    background: var(--sign-white);
    overflow: hidden;
  }
  .block { position: absolute; }
  .block--corner { left: 29px; top: 0; width: 231px; height: 229px; background: var(--brand-yellow); }
  .block--main { left: 188px; top: 383px; width: 538px; height: 706px; background: var(--brand-yellow); }
  .site-photo {
    position: absolute; left: 0; top: 190px; width: 516px; height: 411px;
    background: linear-gradient(180deg, #8fb4e0 0%, #c7d3e6 30%, #f2d79a 50%, #c9a66b 62%, #9c8f7a 80%, #d8c9a4 100%);
  }
  .glaze { position: absolute; background: var(--yellow-glaze); }
  .glaze--corner { left: 29px; top: 190px; width: 231px; height: 39px; }
  .glaze--main { left: 188px; top: 383px; width: 328px; height: 218px; }
  .contour-field {
    position: absolute; left: 0; top: 601px; width: 188px; height: 488px;
    background: var(--contour-bg);
  }
  .brand {
    position: absolute; left: 330px; top: 104px;
    display: flex; align-items: center; gap: 16px;
  }
  .brand__name {
    font-size: 30px; font-weight: 500; letter-spacing: 1px; color: var(--ink);
  }
  .brand__mark {
    width: 58px; height: 58px; border-radius: 50%;
    border: 6px solid var(--brand-yellow);
  }
  .contact { position: absolute; left: 172px; }
  .contact__icon {
    position: absolute; left: 0; top: 0; width: 70px; height: 57px;
    background: var(--icon-olive);
    display: flex; align-items: center; justify-content: center;
  }
  .contact__icon::after {
    content: ""; position: absolute; left: 0; bottom: -12px;
    border-top: 12px solid var(--icon-fold); border-left: 12px solid transparent;
  }
  .contact__text {
    position: absolute; left: 114px; top: 0;
    font-size: 21px; line-height: 28px; white-space: nowrap;
  }
  .contact--phone { top: 659px; }
  .contact--phone .contact__text { top: 5px; }
  .contact--mail { top: 774px; }
  .contact--mail .contact__text { top: 14px; }
  .contact--place { top: 875px; }
  .contact--place .contact__text { top: -2px; }
  .website {
    position: absolute; left: 188px; width: 538px; top: 1004px;
    text-align: center; font-size: 22px; letter-spacing: 3.6px;
  }
</style>
</head>
<body>
  <main class="sign">
    <div class="block block--corner"></div>
    <div class="block block--main"></div>
    <div class="site-photo" role="img" aria-label="Houses under construction with concrete frames and roof trusses at sunset"></div>
    <div class="glaze glaze--corner"></div>
    <div class="glaze glaze--main"></div>
    <div class="contour-field" role="img" aria-label="Faint topographic contour line pattern"></div>

    <div class="brand">
      <span class="brand__name">ZEH CONSTRUCTION</span>
      <span class="brand__mark"></span>
    </div>

    <div class="contact contact--phone">
      <div class="contact__icon">
        <svg width="28" height="28" viewBox="0 0 24 24" fill="#fff"><path d="M6.6 10.8a15.1 15.1 0 0 0 6.6 6.6l2.2-2.2c.3-.3.7-.4 1-.2 1.1.4 2.3.6 3.6.6.6 0 1 .4 1 1V20c0 .6-.4 1-1 1A17 17 0 0 1 3 4c0-.6.4-1 1-1h3.5c.6 0 1 .4 1 1 0 1.3.2 2.5.6 3.6.1.3 0 .7-.2 1z"/></svg>
      </div>
      <p class="contact__text">Direct - 555.014.2271<br>Office - 555.014.3380</p>
    </div>

    <div class="contact contact--mail">
      <div class="contact__icon">
        <svg width="30" height="22" viewBox="0 0 30 22"><rect x="1" y="1" width="28" height="20" fill="#fff"/><path d="M1 1l14 11L29 1" fill="none" stroke="#b4b23c" stroke-width="2"/></svg>
      </div>
      <p class="contact__text">marek@zehconstruction.com</p>
    </div>

    <div class="contact contact--place">
      <div class="contact__icon">
        <svg width="26" height="32" viewBox="0 0 26 32"><path d="M13 1a9 9 0 0 0-9 9c0 7 9 15 9 15s9-8 9-15a9 9 0 0 0-9-9z" fill="#fff"/><circle cx="13" cy="10" r="3.5" fill="#b4b23c"/><ellipse cx="13" cy="29" rx="9" ry="2.2" fill="none" stroke="#fff" stroke-width="1.6"/></svg>
      </div>
      <p class="contact__text">1840 Harbor Way, Ste. 310<br>Palm Crest, FL 33999</p>
    </div>

    <p class="website">www.zehconstruction.com</p>
  </main>
</body>
</html>
```